Logo and Business card design!

Welbrook Estates

We are a Property development and real estate company (needs a logo design).

Welbrook estates is based in Sydney Australia and will be dealing with high net worth individuals with a corporate background. The demographic of clients will be relatively youthful and savvy. We do development finance, property development and some portion of property sales

I'd like the 'Welbrook' part of the name to be strength of the title, with 'property' playing a very minor part, perhaps in tiny font somewhere off to the bottom or side or something

Thank you!

Target Market(s)

25-55 years old

Industry/Entity Type

Real Estate Development

Contact Information for Business Card

Please arrange this information as you see fit

Leon Brightwater
Managing Director
0417 582 273
leon@welbrookestates-example.com.au
www.welbrookestates-example.com.au

Logo Text

Welbrook estates

Font styles to use
Serif

Colors

Designer to choose colors to be used in the design.

Requirements
Must have
• PLEASE VIEW THE UPLOADED IMAGES AND EXAMPLES
• And please put 'property' in small letters at the bottom or to the side. I want it to play a minimalist role, with 'WELBROOK' being the feature
• Colours! Please make sure theyre mostly grey and white with possibly some other dark blue and maybe dark grey
Nice to have
• Please feel free to use whatever colors you like, the suggested colors are something I selected momentarily and dont necessarily reflect strict guidelines
Should not have
• NO pictures or shapes of houses. I dont want the logo design to be so literal in its imagery

```html
<!DOCTYPE html>
<html lang="en">
<head>
<meta charset="utf-8">
<title>Welbrook Estates – Business Card</title>
<link rel="stylesheet" href="https://fonts.googleapis.com/css2?family=Libre+Baskerville&family=Questrial&display=swap">
<style>
  :root {
    --backdrop: #9a9a9a;
    --card-black: #0d0d0d;
    --card-black-soft: #1c1c1c;
    --card-white: #fbfbfb;
    --ink: #1a1a1a;
    --ink-soft: #3a3a3a;
    --rule: #e2e2e2;
    --on-dark: #ffffff;
  }
  * { box-sizing: border-box; margin: 0; padding: 0; }
  html, body {
    width: 1200px;
    height: 982px;
    overflow: hidden;
    background: var(--backdrop);
  }
  .canvas {
    position: relative;
    width: 1200px;
    height: 982px;
    display: flex;
    justify-content: center;
    align-items: center;
    gap: 44px;
  }
  .card {
    position: relative;
    width: 330px;
    height: 540px;
    box-shadow: 0 10px 24px rgba(0, 0, 0, 0.28);
    overflow: hidden;
  }

  /* Front */
  .card-front {
    background: radial-gradient(circle at 30% 25%, var(--card-black-soft), var(--card-black) 70%);
  }
  .front-wordmark {
    position: absolute;
    right: 30px;
    bottom: 40px;
    font-family: "Questrial", sans-serif;
    font-size: 15px;
    letter-spacing: 2px;
    color: var(--on-dark);
    text-align: right;
  }

  /* Back */
  .card-back {
    background: var(--card-black);
    display: flex;
    flex-direction: column;
  }
  .band-top { height: 118px; }
  .contact-panel {
    height: 300px;
    background: var(--card-white);
    display: flex;
    flex-direction: column;
    align-items: center;
    padding-top: 10px;
    color: var(--ink);
  }
  .holder-name {
    font-family: "Libre Baskerville", serif;
    font-size: 19px;
    line-height: 1.2;
  }
  .holder-role {
    font-family: "Questrial", sans-serif;
    font-size: 13px;
    color: var(--ink-soft);
    letter-spacing: 0.5px;
    padding-bottom: 8px;
    border-bottom: 1px solid var(--rule);
    width: 190px;
    text-align: center;
  }
  .contact-item {
    display: flex;
    flex-direction: column;
    align-items: center;
    margin-top: 16px;
    font-family: "Questrial", sans-serif;
    font-size: 13.5px;
    letter-spacing: 0.4px;
  }
  .contact-item:first-of-type { margin-top: 24px; }
  .contact-item svg { width: 18px; height: 18px; margin-bottom: 8px; }
  .contact-item .detail-small { font-size: 11.5px; }
  .band-bottom {
    flex: 1;
    display: flex;
    justify-content: center;
    align-items: center;
  }
  .back-wordmark {
    font-family: "Questrial", sans-serif;
    font-size: 16px;
    letter-spacing: 2px;
    color: var(--on-dark);
  }
</style>
</head>
<body>
<main class="canvas">
  <section class="card card-front" aria-label="Card front">
    <p class="front-wordmark">WELBROOK ESTATES</p>
  </section>

  <section class="card card-back" aria-label="Card back">
    <div class="band-top"></div>
    <div class="contact-panel">
      <h1 class="holder-name">Leon Brightwater</h1>
      <p class="holder-role">Managing Director</p>

      <div class="contact-item">
        <svg viewBox="0 0 20 20" aria-hidden="true">
          <rect x="2" y="1" width="16" height="18" rx="2" fill="var(--ink)"/>
          <path d="M7 5c-1 1-1 3 1 6s4 4 5 3l1-1-2-2-1 1c-1 0-3-2-3-3l1-1-2-2z" fill="var(--card-white)"/>
        </svg>
        <span>0417 582 273</span>
      </div>

      <div class="contact-item">
        <svg viewBox="0 0 20 20" aria-hidden="true">
          <path d="M2 8 10 3l8 5v9H2z" fill="var(--ink)"/>
          <path d="M2 8l8 5 8-5" fill="none" stroke="var(--card-white)" stroke-width="1.3"/>
        </svg>
        <span class="detail-small">leon@welbrookestates-example.com.au</span>
      </div>

      <div class="contact-item">
        <svg viewBox="0 0 20 20" aria-hidden="true">
          <circle cx="10" cy="10" r="8.5" fill="none" stroke="var(--ink)" stroke-width="1.6"/>
          <ellipse cx="10" cy="10" rx="3.5" ry="8.5" fill="none" stroke="var(--ink)" stroke-width="1.3"/>
          <path d="M1.5 10h17M3 5.5h14M3 14.5h14" stroke="var(--ink)" stroke-width="1.2"/>
        </svg>
        <span class="detail-small">www.welbrookestates-example.com.au</span>
      </div>
    </div>
    <div class="band-bottom">
      <p class="back-wordmark">WELBROOK ESTATES</p>
    </div>
  </section>
</main>
</body>
</html>
```